BUSINESS CARD FOR GUITAR SCHOOL

I would like to design a business card for my Guitar Music School. The school is called "Pluck & Meadow".

The card should be yellow.

Target Market(s)

18-35 years old

Industry/Entity Type

School

Contact Information for Business Card

I would like to design a business card for my Guitar Music School. The school is called "Pluck & Meadow". The card should be yellow.

Card must be consistent with my website design: www.pluckandmeadow.com.sg

Requirements
Must have
• 1) Name of Company
• 2) Company Logo
• 3) Name of Employee
• 4) Position of Employee
• 5) Contact Number
• 6) Address
Nice to have
• Creative Design
• Card must be consistent with my website design: www.pluckandmeadow.com.sg
Should not have
• Boring Design

```html
<!DOCTYPE html>
<html lang="en">
<head>
<meta charset="utf-8">
<title>Pluck &amp; Meadow — Business Card</title>
<link rel="stylesheet" href="https://fonts.googleapis.com/css2?family=Arimo:wght@700&family=Oswald:wght@500&display=swap">
<style>
  :root {
    --card-yellow: #fcbf26;
    --body-orange: #f26522;
    --ink-dark: #1a1a1a;
    --ink-grey: #3b3b3b;
    --canvas-bg: #ffffff;
  }
  html, body {
    margin: 0;
    padding: 0;
    width: 1200px;
    height: 740px;
    overflow: hidden;
    background: var(--canvas-bg);
  }
  .business-card {
    display: block;
    width: 1200px;
    height: 740px;
  }
  .guitar-outline { fill: var(--card-yellow); }
  .guitar-face { fill: var(--body-orange); }
  .employee-name {
    font-family: "Arimo", Arial, sans-serif;
    font-weight: 700;
    font-size: 20px;
    fill: var(--ink-dark);
  }
  .employee-role,
  .contact-line {
    font-family: "Arimo", Arial, sans-serif;
    font-weight: 700;
    fill: var(--card-yellow);
  }
  .employee-role { font-size: 17px; }
  .contact-line { font-size: 16px; }
  .contact-icon { fill: var(--ink-grey); }
  .school-name {
    font-family: "Oswald", "Arial Narrow", sans-serif;
    font-weight: 500;
    font-size: 50px;
    fill: var(--ink-grey);
  }
  .website {
    font-family: "Arimo", Arial, sans-serif;
    font-weight: 700;
    font-size: 14px;
    fill: var(--ink-dark);
  }
  .headstock-name {
    font-family: "Arimo", Arial, sans-serif;
    font-weight: 700;
    font-size: 22px;
    fill: var(--ink-grey);
  }
</style>
</head>
<body>
<svg class="business-card" viewBox="0 0 900 555" xmlns="http://www.w3.org/2000/svg" aria-label="Pluck &amp; Meadow guitar-shaped business card">
  <g class="guitar">
    <!-- neck -->
    <rect class="guitar-outline" x="455" y="237" width="250" height="69"/>
    <!-- headstock -->
    <path class="guitar-outline" d="M690 237 C700 232 712 226 726 224 L830 222 C836 228 842 232 850 232 C846 250 846 262 850 272 C844 276 842 284 848 294 C842 300 840 308 846 318 L730 318 C712 316 700 312 690 306 Z"/>
    <!-- body -->
    <path class="guitar-outline" d="M472 237 C474 180 472 120 450 98 C425 78 370 80 332 92 C300 102 285 122 260 122 C236 122 210 92 160 86 C110 80 70 92 58 130 C48 170 50 230 54 290 C58 350 56 400 92 414 C130 428 200 420 232 410 C250 404 262 402 280 410 C310 424 380 428 430 418 C466 410 474 370 472 306 Z"/>
    <path class="guitar-face" d="M448 200 C448 160 440 140 420 134 C390 126 350 128 320 140 C300 148 282 166 260 166 C238 166 214 142 180 138 C140 134 96 136 84 160 C74 190 76 240 78 290 C80 340 84 372 110 378 C150 386 210 380 240 370 C258 364 272 366 290 372 C320 382 380 386 420 376 C444 368 448 340 448 300 Z"/>
  </g>

  <g class="identity">
    <text class="employee-name" x="108" y="186">Mara Lindqvist</text>
    <text class="employee-role" x="146" y="205">Manager</text>
  </g>

  <g class="contact-phone">
    <path class="contact-icon" d="M293 200 C291 204 292 210 296 214 C299 217 303 218 305 216 L303 212 C302 211 300 212 299 212 C297 210 296 207 297 205 C298 204 299 203 298 202 L296 198 Z"/>
    <text class="contact-line" x="306" y="217">0198 765 432</text>
  </g>

  <text class="school-name" x="243" y="292" text-anchor="middle">Pluck &amp; Meadow</text>

  <g class="contact-address">
    <path class="contact-icon" d="M110 346 L119 338 L128 346 L125 346 L125 354 L121 354 L121 349 L117 349 L117 354 L113 354 L113 346 Z"/>
    <text class="contact-line" x="135" y="355">48 Harbour st. Sydney 5490 NSW</text>
  </g>

  <text class="website" x="453" y="279">www.pluckandmeadow.com.sg</text>

  <g class="headstock-brand">
    <text class="headstock-name" x="697" y="272">Pluck &amp;</text>
    <text class="headstock-name" x="712" y="295">Meadow</text>
  </g>
</svg>
</body>
</html>
```